Safety Starts at The Top

Want to make a poster showing our company president in full safety gear (see attached photo) encouraging how "Safety Starts at the Top" We encourage creativity. Visit our website for ideas about our company. www.halvorbuilders.com Our main colors are blue and black, but we will allow other colors to make the poster pop and stand out.

Industry/Entity Type

It Company

Colors
0255a3

Requirements
Must have
• -Must have the photo attached somewhere on the poster. Must have a PPE List which can be creative or bullet points 1. Hard Hat 2. Safety Glasses 3. Shirt with Sleeves, 4. Reflective Vest 5. Gloves 6. Long Pants 7. Safety Boots
• -Must have title "Safety Starts at the Top"
• -Must have a box or section that says the following"Because of our company's core value of RESPECT FOR ALL PEOPLE the commitment to Safety Starts at the Top. Halvor Builders’s most valuable asset is our team members, which is why I take personal responsibility for our safety culture. It is our daily mission for every team member to return home to their families without injuries, giving them a life away from work that can be enjoyed."

```html
<!DOCTYPE html>
<html lang="en">
<head>
<meta charset="utf-8">
<title>Safety Starts at the Top – Halvor Builders</title>
<link rel="stylesheet" href="https://fonts.googleapis.com/css2?family=Alfa+Slab+One&family=Barlow+Condensed:wght@600&family=Roboto+Condensed:ital,wght@1,400&display=swap">
<style>
  :root {
    --navy-deep: #06142e;
    --navy: #0a2a63;
    --brand-blue: #0255a3;
    --title-blue: #1a5cc0;
    --band-black: #000000;
    --white: #ffffff;
    --logo-ink: #14356f;
    --logo-band: #e9eef6;
    --hat-blue: #2f63c4;
    --vest-lime: #c9e04a;
    --pants-khaki: #a8a591;
    --shoe-dark: #2a211c;
  }
  * { margin: 0; padding: 0; box-sizing: border-box; }
  html, body { width: 849px; height: 1200px; overflow: hidden; background: var(--navy-deep); }
  .poster {
    position: relative;
    width: 849px;
    height: 1200px;
    overflow: hidden;
    background: linear-gradient(100deg, var(--navy-deep) 0%, var(--navy) 35%, var(--brand-blue) 75%, #0b5dbb 100%);
  }
  .president-photo {
    position: absolute;
    left: 14px;
    top: 76px;
    width: 478px;
    height: 1100px;
    border-radius: 36px;
    opacity: 0.8;
    background: linear-gradient(180deg,
      var(--hat-blue) 0%,
      #6f8aa8 9%,
      var(--vest-lime) 22%,
      var(--vest-lime) 44%,
      var(--pants-khaki) 52%,
      var(--pants-khaki) 88%,
      var(--shoe-dark) 100%);
  }
  .title-band {
    position: absolute;
    left: 308px;
    top: 28px;
    width: 541px;
    height: 168px;
    background: var(--band-black);
  }
  .title {
    position: absolute;
    left: 352px;
    top: 30px;
    font-family: "Alfa Slab One", serif;
    font-weight: 400;
    color: var(--white);
    line-height: 1;
  }
  .title .line-1 { display: block; font-size: 49px; letter-spacing: 1px; }
  .title .line-2 { display: inline-block; font-size: 45px; margin-top: 2px; vertical-align: top; }
  .title .line-top {
    position: absolute;
    left: 150px;
    top: 50px;
    font-size: 138px;
    color: var(--title-blue);
    letter-spacing: -1px;
  }
  .leaders { position: absolute; inset: 0; }
  .ppe-list {
    position: absolute;
    left: 530px;
    top: 0;
    list-style: none;
    font-family: "Barlow Condensed", sans-serif;
    font-weight: 600;
    font-size: 27px;
    color: var(--white);
  }
  .ppe-list li { position: absolute; white-space: nowrap; transform: translateY(-50%); }
  .ppe-list .small { font-size: 24px; }
  .president-quote {
    position: absolute;
    left: 506px;
    top: 886px;
    width: 314px;
    font-family: "Roboto Condensed", sans-serif;
    font-style: italic;
    font-size: 14.6px;
    letter-spacing: -0.15px;
    line-height: 21px;
    color: var(--white);
    text-align: justify;
  }
  .quote-mark {
    position: absolute;
    font-family: "Alfa Slab One", serif;
    font-size: 72px;
    color: var(--white);
    line-height: 1;
  }
  .quote-open { left: 468px; top: 872px; }
  .quote-close { left: 726px; top: 1036px; }
  .brand-band {
    position: absolute;
    left: 472px;
    top: 1076px;
    width: 377px;
    height: 108px;
    background: linear-gradient(90deg, rgba(233,238,246,0) 0%, var(--logo-band) 25%, var(--logo-band) 100%);
  }
  .brand-name {
    position: absolute;
    left: 506px;
    top: 1090px;
    display: flex;
    align-items: center;
    gap: 14px;
    font-family: "Barlow Condensed", sans-serif;
    font-weight: 600;
    color: var(--logo-ink);
  }
  .brand-square { width: 78px; height: 78px; background: var(--logo-ink); }
  .brand-words { font-size: 46px; line-height: 40px; letter-spacing: 1px; }
</style>
</head>
<body>
<div class="poster">
  <div class="president-photo" role="img" aria-label="Photo of the company president standing hands on hips in full safety gear: blue hard hat, safety glasses, checked shirt, high-visibility reflective vest, work gloves, khaki long pants and safety shoes"></div>

  <div class="title-band"></div>
  <h1 class="title">
    <span class="line-1">SAFETY STARTS</span>
    <span class="line-2">at the</span>
    <span class="line-top">TOP</span>
  </h1>

  <svg class="leaders" width="849" height="1200" viewBox="0 0 849 1200" aria-hidden="true">
    <g fill="none" stroke="#ffffff" stroke-width="2">
      <polyline points="318,145 469,145 469,252 514,252"/>
      <polyline points="312,174 444,174 444,326 514,326"/>
      <polyline points="426,400 514,400"/>
      <polyline points="350,474 514,474"/>
      <polyline points="446,548 514,548"/>
      <polyline points="392,698 444,698 444,622 514,622"/>
      <polyline points="428,1120 466,1120 466,696 514,696"/>
    </g>
    <g fill="#ffffff">
      <circle cx="318" cy="145" r="5"/><circle cx="514" cy="252" r="5"/>
      <circle cx="312" cy="174" r="5"/><circle cx="514" cy="326" r="5"/>
      <circle cx="426" cy="400" r="5"/><circle cx="514" cy="400" r="5"/>
      <circle cx="350" cy="474" r="5"/><circle cx="514" cy="474" r="5"/>
      <circle cx="446" cy="548" r="5"/><circle cx="514" cy="548" r="5"/>
      <circle cx="392" cy="698" r="5"/><circle cx="514" cy="622" r="5"/>
      <circle cx="428" cy="1120" r="5"/><circle cx="514" cy="696" r="5"/>
    </g>
  </svg>

  <ul class="ppe-list">
    <li style="top:252px">HELMET</li>
    <li style="top:326px">SAFETY GLASSES</li>
    <li style="top:400px">SHIRTS <span class="small">with</span> SLEEVES</li>
    <li style="top:474px">REFLECTIVE VEST</li>
    <li style="top:548px">GLOVES</li>
    <li style="top:622px">LONG PANTS</li>
    <li style="top:696px">SAFETY SHOES</li>
  </ul>

  <span class="quote-mark quote-open">“</span>
  <p class="president-quote">Because of our company's core value of RESPECT FOR ALL PEOPLE the commitment to Safety Starts at the Top. Halvor Builders’s most valuable asset is our team members, which is why I take personal responsibility for our safety culture. It is our daily mission for every team member to return home to their families without injuries, giving them a life away from work that can be enjoyed.</p>
  <span class="quote-mark quote-close">”</span>

  <div class="brand-band"></div>
  <div class="brand-name">
    <span class="brand-square"></span>
    <span class="brand-words">HALVOR<br>BUILDERS</span>
  </div>
</div>
</body>
</html>
```